VELMOTIK Amazing Business Cards Challenge

Velmoti is a new technology company that will provide engineering and manufacturing services in the electric vehicle industry.

We are looking at a new business card that will support our orientation in providing advanced, innovative solutions. The business card will be lean and present the only information required to be more efficient.

Target Market(s)

Fleet operators, private commercial vehicle operators, delivery companies.

Industry/Entity Type

Business

Contact Information for Business Card

Use the logo and its colors, use a white background.

Font styles to use
Sans Serif

Colors
0455a3
ffffff
9bcb3c

Requirements
Must have
• Velmotik Logo
• All informations in the DOC file = 3 different cards.
• White background
Nice to have
• Icons for email, phone and web address.
• Cute design and strong identity.
Should not have
• Bleeds

```html
<!DOCTYPE html>
<html lang="fr">
<head>
<meta charset="utf-8">
<title>Velmotik – Cartes professionnelles</title>
<link rel="stylesheet" href="https://fonts.googleapis.com/css2?family=Audiowide&family=Open+Sans:wght@400;600&display=swap">
<style>
  :root {
    --brand-blue: #0455a3;
    --brand-green: #9bcb3c;
    --card-white: #ffffff;
    --backdrop: #e6ecef;
    --title-grey: #8a8f94;
    --address-grey: #6b7076;
  }
  * { box-sizing: border-box; margin: 0; padding: 0; }
  html, body { width: 1200px; height: 719px; overflow: hidden; }
  body { background: var(--backdrop); position: relative; font-family: "Open Sans", Arial, sans-serif; }

  .card {
    position: absolute; top: 200px; width: 560px; height: 320px;
    background: var(--card-white);
    box-shadow: 0 6px 18px rgba(0,0,0,.12);
    overflow: hidden;
  }
  .card--vp { left: 20px; }
  .card--ceo { left: 620px; }

  .identity { position: absolute; left: 34px; top: 46px; }
  .identity__name {
    font-family: "Audiowide", "Open Sans", sans-serif;
    color: var(--brand-blue); font-size: 21px; letter-spacing: 1px; text-transform: lowercase;
  }
  .identity__name .credentials { font-family: "Open Sans", sans-serif; font-size: 13px; letter-spacing: .5px; text-transform: none; }
  .identity__title { font-size: 9px; color: var(--title-grey); letter-spacing: .6px; margin-top: 2px; text-transform: uppercase; }
  .identity__title span + span { margin-left: 10px; }

  .contact-band {
    position: absolute; left: 0; right: 0; top: 100px; height: 118px;
    background: var(--brand-blue);
    border-top: 3px solid var(--brand-green);
    border-bottom: 3px solid var(--brand-green);
    display: flex;
  }
  .contact {
    flex: 1; display: flex; flex-direction: column; align-items: center; justify-content: center;
    gap: 12px; color: var(--card-white); font-size: 11.5px; letter-spacing: .3px;
  }
  .contact + .contact { border-left: 2px dashed rgba(255,255,255,.85); margin: 10px 0; }
  .contact__icon { width: 56px; height: 50px; }

  .brand { position: absolute; left: 0; right: 0; top: 240px; text-align: center; }
  .brand__mark { display: inline-flex; align-items: center; gap: 7px; }
  .brand__dot { width: 14px; height: 14px; border-radius: 50%; background: var(--brand-blue); }
  .brand__name { font-size: 22px; font-weight: 600; color: var(--brand-blue); letter-spacing: .5px; }
  .brand__address { font-size: 7.5px; color: var(--address-grey); letter-spacing: .4px; margin-top: 8px; text-transform: uppercase; }
</style>
</head>
<body>

<svg width="0" height="0" style="position:absolute" aria-hidden="true">
  <defs>
    <polygon id="hex" points="14,0 42,0 56,25 42,50 14,50 0,25" fill="#ffffff"/>
  </defs>
</svg>

<article class="card card--vp">
  <header class="identity">
    <h1 class="identity__name">Mathis Leclerc</h1>
    <p class="identity__title"><span>V.P. Développement des affaires</span><span>V.P. Business Development</span></p>
  </header>
  <section class="contact-band">
    <div class="contact contact--phone">
      <svg class="contact__icon" viewBox="0 0 56 50" aria-hidden="true"><use href="#hex"/><rect x="20" y="11" width="16" height="28" rx="3" fill="none" stroke="#0455a3" stroke-width="2.5"/><circle cx="28" cy="35" r="1.3" fill="#0455a3"/></svg>
      <span>+1.514.555.0148</span>
    </div>
    <div class="contact contact--email">
      <svg class="contact__icon" viewBox="0 0 56 50" aria-hidden="true"><use href="#hex"/><rect x="15" y="15" width="26" height="19" fill="#0455a3"/><polyline points="15,15 28,27 41,15" fill="none" stroke="#ffffff" stroke-width="2"/></svg>
      <span>mleclerc@velmotik.com</span>
    </div>
    <div class="contact contact--web">
      <svg class="contact__icon" viewBox="0 0 56 50" aria-hidden="true"><use href="#hex"/><text x="28" y="29" text-anchor="middle" font-family="Open Sans, sans-serif" font-weight="600" font-size="10" fill="#0455a3">www</text></svg>
      <span>velmotik.com</span>
    </div>
  </section>
  <footer class="brand">
    <div class="brand__mark"><span class="brand__dot"></span><span class="brand__name">velmotik</span></div>
    <p class="brand__address">210 - 480 Rue Laurier Est, Montréal (QC) H2J 1E5 Canada</p>
  </footer>
</article>

<article class="card card--ceo">
  <header class="identity">
    <h1 class="identity__name">Julien Bérubé, <span class="credentials">ing., M.Sc.A.</span></h1>
    <p class="identity__title"><span>Président | CEO</span></p>
  </header>
  <section class="contact-band">
    <div class="contact contact--phone">
      <svg class="contact__icon" viewBox="0 0 56 50" aria-hidden="true"><use href="#hex"/><rect x="20" y="11" width="16" height="28" rx="3" fill="none" stroke="#0455a3" stroke-width="2.5"/><circle cx="28" cy="35" r="1.3" fill="#0455a3"/></svg>
      <span>+1.514.555.0173</span>
    </div>
    <div class="contact contact--email">
      <svg class="contact__icon" viewBox="0 0 56 50" aria-hidden="true"><use href="#hex"/><rect x="15" y="15" width="26" height="19" fill="#0455a3"/><polyline points="15,15 28,27 41,15" fill="none" stroke="#ffffff" stroke-width="2"/></svg>
      <span>jberube@velmotik.com</span>
    </div>
    <div class="contact contact--web">
      <svg class="contact__icon" viewBox="0 0 56 50" aria-hidden="true"><use href="#hex"/><text x="28" y="29" text-anchor="middle" font-family="Open Sans, sans-serif" font-weight="600" font-size="10" fill="#0455a3">www</text></svg>
      <span>velmotik.com</span>
    </div>
  </section>
  <footer class="brand">
    <div class="brand__mark"><span class="brand__dot"></span><span class="brand__name">velmotik</span></div>
    <p class="brand__address">210 - 480 Rue Laurier Est, Montréal (QC) H2J 1E5 Canada</p>
  </footer>
</article>

</body>
</html>
```